I need a website built for my organization.
We are the world's largest network of music producers.
The website should be professional, sharp, and high quality., We need a website built for The Halvern Sound Guild. We are one of the World's largest association of music producers.
The site must be professional, sharp, and high quality., I need a website built for my organization.
The site must be professional, sharp, and high quality.
Somewhere in the top half of the site there should be a form for the user to fill out. The details of the form are as follows:
Title (large and bold): Contact Us or Submit Your Music
Fields to include (* = required): First Name*, Last Name*, Age, Zip Code, Email Address*, Daytime Phone, Evening Phone, Comments
Then, there will be a "submit" button to proceed to next step of form. Just below the "submit" button, should be the following verbiage: "After submitting, you will have the opportunity to upload demos of your music (optional) and provide other pertinent information about yourself, band, or group."
Target Market(s)
Music producers and aspiring musicians
Industry/Entity Type
Group
Colors
Designer to choose colors to be used in the design.
Look and feel

```html
<!DOCTYPE html>
<html lang="en">
<head>
<meta charset="utf-8">
<title>Halvern Sound Guild</title>
<link href="https://fonts.googleapis.com/css2?family=Josefin+Sans:wght@400;600&family=Poiret+One&family=Marcellus&family=Roboto:wght@400;500&family=Roboto+Condensed:ital,wght@0,300;0,400;0,700;1,700&display=swap" rel="stylesheet">
<style>
:root{
  --nav-bg:#121212;
  --page-bg:#1b1b1b;
  --footer-bg:#1e1e1e;
  --panel:#ffffff;
  --ink:#222222;
  --muted:#8a8a8a;
  --accent:#2a9fd6;
  --form-blue:#1386ba;
  --form-edge:#0d6d99;
  --required:#c0392b;
  --tile-dark:#1c1c1c;
}
*{box-sizing:border-box;margin:0;padding:0}
html,body{width:980px;height:1200px;overflow:hidden}
body{background:var(--page-bg);font-family:"Roboto",sans-serif;color:var(--ink);position:relative}

.site-header{position:absolute;left:0;top:0;width:980px;height:68px;background:var(--nav-bg)}
.brand{position:absolute;left:35px;top:20px;color:#fff;font-family:"Josefin Sans",sans-serif;font-weight:600;font-size:21px;letter-spacing:1px}
.main-nav{position:absolute;right:36px;top:27px;display:flex;gap:35px}
.main-nav a{font-family:"Marcellus",serif;font-size:11.5px;color:#c9c9c9;text-decoration:none;letter-spacing:.4px;position:relative}
.main-nav a.active{color:var(--accent)}
.main-nav a.active::after{content:"";position:absolute;left:0;right:0;bottom:-6px;height:3px;background:var(--accent)}

.hero{position:absolute;left:0;top:68px;width:980px;height:440px;
  background:radial-gradient(ellipse at 20% 40%,#b0204a 0%,rgba(120,20,60,.6) 35%,transparent 60%),
  radial-gradient(ellipse at 75% 30%,#2a3fd0 0%,rgba(40,40,160,.7) 40%,transparent 70%),
  linear-gradient(90deg,#4a0f2a 0%,#3a1460 50%,#101a70 100%)}
.hero-tagline{position:absolute;left:0;width:980px;top:120px;text-align:center;color:#fff;font-family:"Josefin Sans",sans-serif;font-weight:600;font-size:14px;letter-spacing:4.5px;display:flex;justify-content:center;align-items:center;gap:22px}
.hero-tagline::before,.hero-tagline::after{content:"";width:82px;height:1px;background:#fff}
.hero-box{position:absolute;left:240px;top:158px;width:501px;height:112px;background:rgba(5,5,15,.82);border:1px solid rgba(255,255,255,.18);color:#fff;font-family:"Poiret One",sans-serif;font-size:33px;line-height:38px;text-align:center;padding-top:16px;letter-spacing:1px;text-transform:uppercase}
.hero-cta{position:absolute;left:420px;top:294px;width:140px;height:29px;background:linear-gradient(#2fb0e0,#147fb0);transform:skewX(-12deg);color:#fff;font-family:"Josefin Sans",sans-serif;font-weight:600;font-size:11.5px;letter-spacing:2.5px;text-align:center;line-height:31px}
.hero-cta span{display:inline-block;transform:skewX(12deg)}
.slider-dots{position:absolute;left:430px;top:398px;display:flex;gap:4px}
.slider-dots i{width:6px;height:6px;border-radius:50%;background:#fff;display:block}

.content-panel{position:absolute;left:35px;top:508px;width:910px;height:516px;background:var(--panel)}
.news-tile{position:absolute;left:3px;top:4px;width:166px;height:169px;background:var(--tile-dark)}
.news-tile h2{position:absolute;right:15px;top:13px;font-family:"Marcellus",serif;font-weight:400;font-size:16px;color:#fff}
.news-arrows{position:absolute;left:80px;top:44px;display:flex;gap:2px}
.news-arrows span{width:34px;height:32px;background:#111;display:flex;align-items:center;justify-content:center}
.news-card{position:absolute;top:4px;width:241px;height:169px;background:#fff;box-shadow:inset 0 0 18px rgba(0,0,0,.12);text-align:center}
.news-card time{display:block;margin-top:34px;font-family:"Marcellus",serif;font-size:10.5px;color:#222}
.news-card h3{margin-top:7px;font-family:"Marcellus",serif;font-weight:400;font-size:16px;line-height:20px;color:#111}
.news-card hr{width:74px;margin:14px auto 0;border:0;border-top:2px solid #222}
.news-card a{display:block;margin-top:12px;font-family:"Marcellus",serif;font-size:9px;letter-spacing:.8px;color:#222;text-decoration:none}
.welcome{position:absolute;left:22px;top:195px;width:600px}
.welcome .kicker{font-family:"Marcellus",serif;font-size:15px;color:#666}
.welcome h1{font-family:"Marcellus",serif;font-weight:400;font-size:20px;color:#111;margin-bottom:16px}
.welcome p{font-size:11px;line-height:17px;color:#333;margin-bottom:16px}

.contact-form{position:absolute;left:700px;top:480px;width:245px;height:470px;background:var(--form-blue);border-left:4px solid var(--form-edge);border-bottom:4px solid var(--form-edge);box-shadow:-2px 3px 6px rgba(0,0,0,.4);padding:14px 14px 0 11px;font-family:"Roboto Condensed",sans-serif}
.contact-form h2{color:#fff;line-height:29px;margin-bottom:15px}
.contact-form h2 .light{display:block;font-weight:300;font-size:30px}
.contact-form h2 .bold{display:block;font-weight:700;font-size:27px}
.field{background:#fff;border-radius:2px;height:28px;font-size:11.5px;color:#222;padding:7px 10px;margin-bottom:8px}
.field b{color:var(--required);font-weight:400}
.field-row{display:flex;gap:8px}
.field-row .field{flex:1}
.field-row .narrow{flex:0 0 46px}
.field.comments{height:66px}
.submit-btn{height:49px;background:linear-gradient(#2a2a2a,#050505);border-radius:2px;color:#fff;font-weight:300;font-size:29px;display:flex;align-items:center;justify-content:center;gap:6px;margin-top:8px}
.form-note{color:#fff;font-style:italic;font-weight:700;font-size:10.5px;line-height:13.5px;margin-top:7px}

.site-footer{position:absolute;left:0;top:1045px;width:980px;height:155px;background:var(--footer-bg)}
.footer-col{position:absolute;top:0;height:105px;border-right:1px solid #2c2c2c}
.footer-brand{left:0;width:254px;padding:24px 0 0 58px}
.footer-brand .name{font-family:"Josefin Sans",sans-serif;font-weight:600;font-size:16px;color:#9a9a9a;line-height:20px}
.footer-brand small{display:block;margin-top:36px;font-size:10px;color:#9a9a9a}
.footer-contact{left:254px;width:233px;padding:20px 0 0 56px}
.footer-links{left:487px;width:213px;padding:20px 0 0 69px}
.footer-col p{font-size:10px;color:#8a8a8a;line-height:20px}
.footer-social{position:absolute;left:756px;top:27px;display:flex;gap:9px}
.footer-social i{width:26px;height:26px;border-radius:50%;background:#3a3a3a;display:block}
</style>
</head>
<body>
<header class="site-header">
  <div class="brand">Halvern Sound Guild</div>
  <nav class="main-nav">
    <a href="#" class="active">HOME</a>
    <a href="#">ABOUT</a>
    <a href="#">EVENTS</a>
    <a href="#">GALLERY</a>
    <a href="#">NEW MUSIC BOX</a>
    <a href="#">MUSICIAN STORIES</a>
  </nav>
</header>

<section class="hero" role="img" aria-label="Live band performing on a stage lit in red and blue light">
  <div class="hero-tagline">TAKING THE HSG AWARDS TO A NEW LEVEL</div>
  <div class="hero-box">It's amazing what you can<br>see with your ears</div>
  <div class="hero-cta"><span>READ MORE</span></div>
  <div class="slider-dots"><i></i><i></i><i></i><i></i><i></i><i></i><i></i><i></i><i></i><i></i><i></i><i></i></div>
</section>

<main class="content-panel">
  <div class="news-tile">
    <h2>News &amp; Events</h2>
    <div class="news-arrows">
      <span><svg width="8" height="10" viewBox="0 0 8 10"><path d="M6 1L2 5l4 4" stroke="#ccc" fill="none" stroke-width="1.3"/></svg></span>
      <span><svg width="8" height="10" viewBox="0 0 8 10"><path d="M2 1l4 4-4 4" stroke="#ccc" fill="none" stroke-width="1.3"/></svg></span>
    </div>
  </div>
  <article class="news-card" style="left:174px">
    <time>30. 10. 2013</time>
    <h3>Neque porro quis<br>quam est qui dolorem</h3>
    <hr><a href="#">READ MORE</a>
  </article>
  <article class="news-card" style="left:420px">
    <time>30. 10. 2013</time>
    <h3>Neque porro quis<br>quam est qui dolorem</h3>
    <hr><a href="#">READ MORE</a>
  </article>
  <div class="welcome">
    <div class="kicker">Welcome to</div>
    <h1>Halvern Sound Guild</h1>
    <p>Lorem Ipsum is simply dummy text of the printing and typesetting industry. Lorem Ipsum has been the industry's standard dummy text ever since the 1500s, when an unknown printer took a galley of type and scrambled it to make a type specimen book. It has survived not only five centuries, but also the leap into electronic typesetting, remaining essentially unchanged.</p>
    <p>It was popularised in the 1960s with the release of Pressmark sheets containing Lorem Ipsum passages, and more recently with desktop publishing software like Quillset Layout including versions of Lorem Ipsum.</p>
    <p>The standard chunk of Lorem Ipsum used since the 1500s is reproduced below for those interested. Sections 1.10.32 and 1.10.33 from "de Finibus Bonorum et Malorum" by Orvel Tansby are also reproduced in their exact original form, accompanied by English versions from the 1914 translation by H. Ramsden.</p>
  </div>
</main>

<aside class="contact-form">
  <h2><span class="light">Contact Us or</span><span class="bold">Submit Your Music</span></h2>
  <div class="field">First Name<b>*</b>:</div>
  <div class="field">Last Name<b>*</b>:</div>
  <div class="field">Email Adres<b>*</b>:</div>
  <div class="field-row"><div class="field narrow">Age:</div><div class="field">Zip Code:</div></div>
  <div class="field-row"><div class="field">Daytime Phone:</div><div class="field">Evening Phone:</div></div>
  <div class="field comments">Leave Your Comments:</div>
  <div class="submit-btn">submit <svg width="18" height="20" viewBox="0 0 18 20"><path d="M2 2l8 8-8 8M8 2l8 8-8 8" stroke="#777" fill="none" stroke-width="1.4"/></svg></div>
  <p class="form-note">After submitting, you will have the opportunity to upload demos of your music (optional) and provide other pertinent information about yourself, band, or group.</p>
</aside>

<footer class="site-footer">
  <div class="footer-col footer-brand">
    <div class="name">Halvern Sound Guild</div>
    <small>Copyright © 2013</small>
  </div>
  <div class="footer-col footer-contact">
    <p>90, Street Name</p>
    <p>Country Name. 123458</p>
    <p>(+01)-234-5678</p>
    <p>info@halvernguild.org</p>
  </div>
  <div class="footer-col footer-links">
    <p>Join Our Mailing List</p>
    <p>FAQ</p>
    <p>Musician Stories</p>
  </div>
  <div class="footer-social"><i></i><i></i><i></i><i></i><i></i></div>
</footer>
</body>
</html>
```